Webbanner-Design für Slideshow
Zielgruppe
Annegret bietet 3 Kurse an:
diese Kurse verhelfen einem selbst seine Schutzengel wieder zu hören,
mit ihnen ihren Seelenplan weshalb man auf Erden ist zu sehen,
sowie professionell umzusetzen.
Zielgruppe:
Spirituelle Menschen,
welche Engel lieben,
an sich mental gerne in Kursen & Privat arbeiten,
neues Wissen sich liebend gerne aneignen,
ihren Seelenplan wissen und umsetzen möchten,
die Schönheit im Inneren (Seele) und
im Aussen (Körper & Umgebung) lieben.
Aufgabenstellung
Produktbannerbild für meine Website (Slideshow):
Hintergrund: vorhanden in Form von einem Jpeg, hier auf diesem Foto bitte dich einfach mit folgendem beschäftigen:
Schriftzug groß: Engel (wieder) hören lernen & deinen Seelenplan umsetzen
mit Annegret Holzmeier (klein, oder großer Schriftzug?)
Schriftzug klein: mehr …
Schriftfarbe: weiss
Schriftart: moderne Schrift (z.Bsp. was die Zeitschriften benützen)
Haus Button Schriftzug: KURSE IN MUC
Buttons Ideen, Vierecke oder Kreise ect.: Transparent bitte und in passender Farbe
Stil: Modern, klar, schön, nicht verschnörkelt, unesoterisch, unverspielt
Mein Logo mit Flügel: irgendwo miteinbauen
Sonstiges: anbei noch ein Iconzeichen für Kurse Seminar
Auflösung Farbe: Text & Icons für Druck (Flyer) & Webproduktpräsentation (Slideshow)
Maße: (bei 1600xca.872 px., bleiben, Banner nicht verkleinern, oder ranzoomen)

```html
<!DOCTYPE html>
<html lang="de">
<head>
<meta charset="utf-8">
<title>Engel hören lernen – Kursbanner</title>
<link rel="stylesheet" href="https://fonts.googleapis.com/css2?family=Cinzel:wght@400;500&display=swap">
<style>
  :root {
    --rose-deep: #c9adae;
    --rose-mid: #dcc8c8;
    --rose-light: #eee3e2;
    --haze: #f7f2f1;
    --white: #ffffff;
    --shadow: rgba(120, 80, 80, 0.25);
  }
  * { margin: 0; padding: 0; box-sizing: border-box; }
  html, body { width: 1200px; height: 654px; overflow: hidden; }
  body { font-family: "Cinzel", "Trajan Pro", serif; }

  .banner {
    position: relative;
    width: 1200px;
    height: 654px;
    overflow: hidden;
    background:
      radial-gradient(ellipse 600px 320px at 780px 60px, rgba(255,255,255,0.55), transparent 70%),
      linear-gradient(100deg, var(--rose-deep) 0%, var(--rose-mid) 40%, var(--rose-light) 65%, var(--haze) 100%);
  }

  .photo-area {
    position: absolute;
    left: 620px;
    top: 0;
    width: 580px;
    height: 654px;
    background:
      radial-gradient(ellipse 170px 240px at 285px 400px, rgba(236, 210, 205, 0.9), transparent 75%),
      linear-gradient(180deg, #f4eeee 0%, #ece2e1 45%, #f2ebea 100%);
    -webkit-mask-image: linear-gradient(90deg, transparent 0%, #000 28%);
    mask-image: linear-gradient(90deg, transparent 0%, #000 28%);
  }

  .light-band {
    position: absolute;
    left: 0;
    top: 505px;
    width: 640px;
    height: 149px;
    background: linear-gradient(90deg, rgba(255,255,255,0.22), rgba(255,255,255,0.08) 70%, transparent);
  }

  .brand {
    position: absolute;
    left: 22px;
    top: 26px;
    width: 90px;
    text-align: center;
    color: var(--white);
  }
  .brand-dot {
    display: block;
    width: 52px;
    height: 52px;
    margin: 0 auto 8px;
    border: 2px solid var(--white);
    border-radius: 50%;
  }
  .brand-name { font-size: 11px; letter-spacing: 0.5px; }

  .headline {
    position: absolute;
    left: 21px;
    top: 44px;
    color: var(--white);
    text-shadow: 0 1px 3px var(--shadow);
    font-weight: 400;
  }
  .headline-main {
    display: block;
    margin-left: 104px;
    font-size: 104px;
    line-height: 1;
    letter-spacing: 1px;
  }
  .headline-sub {
    display: block;
    margin-top: 22px;
    font-size: 37px;
    line-height: 34px;
    text-transform: lowercase;
  }
  .headline-sub .cap { text-transform: none; }

  .host {
    position: absolute;
    left: 24px;
    top: 312px;
    color: var(--white);
    font-size: 31px;
    text-shadow: 0 1px 3px var(--shadow);
  }

  .course-button {
    position: absolute;
    left: 26px;
    top: 522px;
    display: flex;
    align-items: center;
    gap: 20px;
    color: var(--white);
    text-decoration: none;
  }
  .course-button svg { display: block; }
  .course-button-label {
    font-size: 34px;
    letter-spacing: 0.5px;
    text-shadow: 0 1px 3px var(--shadow);
  }
</style>
</head>
<body>
<main class="banner">
  <div class="photo-area" role="img" aria-label="Foto: Kursleiterin am Schreibtisch vor einem weißen Kaminsims mit Rosen und Dekoration, in hellem Rosé-Licht"></div>
  <div class="light-band"></div>

  <div class="brand">
    <span class="brand-dot"></span>
    <span class="brand-name">Seelenlicht</span>
  </div>

  <h1 class="headline">
    <span class="headline-main">ENGEL</span>
    <span class="headline-sub">(wieder) hören lernen<br>&amp; deinen <span class="cap">S</span>eelenplan<br>umsetzen</span>
  </h1>

  <p class="host">mit Annegret Holzmeier</p>

  <a class="course-button" href="#kurse">
    <svg width="106" height="106" viewBox="0 0 106 106" aria-hidden="true">
      <circle cx="53" cy="53" r="50" fill="rgba(255,255,255,0.08)" stroke="#ffffff" stroke-width="3"/>
      <path d="M22 54 L53 28 L84 54" fill="none" stroke="#ffffff" stroke-width="6" stroke-linejoin="round" stroke-linecap="round"/>
      <rect x="68" y="30" width="7" height="14" fill="#ffffff"/>
      <path d="M32 54 L53 37 L74 54 V78 H59 V63 H47 V78 H32 Z" fill="#ffffff"/>
    </svg>
    <span class="course-button-label">KURSE IN MUC</span>
  </a>
</main>
</body>
</html>
```